Weight Loss water drink label for "Golden Reed Glow" drinks

We need a label design for our new exciting water based weight loss drink called " Golden Reed Glow " weight loss water. It is a carb blocking, calorie burning health drink that assists in weight loss amongst men and woman. The drink is 100% natural with no sugar added. The drink comes in flavours like refreshing lemon, tropical berry and smooth strawberry. The label is for a 500ml bottle and needs to incorporate text on the label. I have uploaded a previous design to the task but feel free to be creative if you have a better idea. the label needs to stand out in the crowd and also be simple and use colour. The label has to appeal to the general public.

Target Market(s)

Our target market is men and woman between the ages of 18 and 65 that are either interested in losing weight or a living healthy

Industry/Entity Type

Health And Wellness

Font styles to use
Script

Requirements
Must have
• Must have the title " Golden Reed Glow " weight loss drink on the label as the title
• Must be a complete label design for a 500ml water bottle.
• Must have colour
• Must be unique
Nice to have
• The shape of a man and a woman's in shape physique as part of the label, not the same shapes used in the uploaded design, must look more details.
Should not have
• No colour or creativity

```html
<!DOCTYPE html>
<html lang="en">
<head>
<meta charset="UTF-8">
<title>Golden Reed Glow – Weight Loss Water Label</title>
<link rel="stylesheet" href="https://fonts.googleapis.com/css2?family=Archivo+Black&family=Archivo:wght@600;800&display=swap">
<style>
  :root {
    --page: #ffffff;
    --red-deep: #a80f12;
    --red: #e31e24;
    --orange: #f2561c;
    --amber: #ffb52e;
    --glow: #ffe27a;
    --ink: #0d0c0c;
    --light: #fff6e0;
    --lime: #c8ff3c;
  }
  html, body {
    margin: 0;
    padding: 0;
    width: 1200px;
    height: 1000px;
    overflow: hidden;
    background: var(--page);
  }
  .canvas {
    position: relative;
    width: 1200px;
    height: 1000px;
    background: var(--page);
  }
  .label {
    position: absolute;
    left: 303px;
    top: 282px;
    width: 594px;
    height: 436px;
    overflow: hidden;
    font-family: "Archivo", "Arial", sans-serif;
    background:
      radial-gradient(ellipse 55% 60% at 45% 40%, rgba(242, 86, 28, 0.85) 0%, rgba(242, 86, 28, 0) 70%),
      linear-gradient(90deg, var(--red-deep) 0%, var(--red) 18%, var(--red) 80%, var(--red-deep) 100%);
  }
  .label__streaks {
    position: absolute;
    inset: 0;
    background:
      linear-gradient(125deg, rgba(255,181,46,0) 30%, rgba(255,226,122,0.35) 42%, rgba(255,181,46,0) 48%),
      linear-gradient(125deg, rgba(255,181,46,0) 48%, rgba(255,226,122,0.4) 55%, rgba(255,181,46,0) 62%),
      linear-gradient(125deg, rgba(255,181,46,0) 64%, rgba(255,226,122,0.25) 69%, rgba(255,181,46,0) 74%);
  }
  .label__kicker,
  .label__title,
  .label__subtitle {
    position: absolute;
    left: 73px;
    margin: 0;
    color: var(--ink);
    text-transform: uppercase;
    line-height: 1;
    white-space: nowrap;
  }
  .label__kicker {
    top: 25px;
    font-family: "Archivo Black", "Arial Black", sans-serif;
    font-size: 21px;
  }
  .label__title {
    top: 52px;
    font-family: "Archivo Black", "Arial Black", sans-serif;
    font-size: 36px;
  }
  .label__subtitle {
    top: 95px;
    font-weight: 800;
    font-size: 13px;
    letter-spacing: 3px;
    color: var(--light);
  }
  .label__athletes {
    position: absolute;
    left: 90px;
    top: 118px;
    width: 330px;
    height: 318px;
    background:
      radial-gradient(ellipse 40% 30% at 50% 22%, rgba(255, 226, 122, 0.7) 0%, rgba(255, 226, 122, 0) 100%),
      radial-gradient(ellipse 50% 42% at 50% 62%, rgba(255, 181, 46, 0.75) 0%, rgba(242, 86, 28, 0) 100%);
  }
  .label__facts {
    position: absolute;
    left: 440px;
    top: 128px;
    width: 140px;
    color: var(--light);
  }
  .facts__claims {
    list-style: none;
    margin: 0 0 16px;
    padding: 0;
  }
  .facts__claim {
    display: flex;
    align-items: center;
    gap: 6px;
    font-weight: 800;
    font-size: 11px;
    text-transform: uppercase;
    line-height: 1;
    margin-bottom: 9px;
  }
  .facts__tick {
    width: 12px;
    height: 12px;
    flex: none;
  }
  .facts__heading {
    margin: 0 0 7px;
    font-family: "Archivo Black", "Arial Black", sans-serif;
    font-size: 11px;
    text-transform: uppercase;
    color: var(--ink);
  }
  .facts__flavours {
    list-style: none;
    margin: 0;
    padding: 0;
  }
  .facts__flavour {
    font-weight: 600;
    font-size: 11px;
    line-height: 1;
    margin-bottom: 7px;
  }
  .facts__flavour::before {
    content: "";
    display: inline-block;
    width: 6px;
    height: 6px;
    border-radius: 50%;
    background: var(--lime);
    margin-right: 6px;
    vertical-align: 1px;
  }
  .label__volume {
    position: absolute;
    right: 20px;
    bottom: 18px;
    margin: 0;
    font-family: "Archivo Black", "Arial Black", sans-serif;
    font-size: 26px;
    line-height: 1;
    color: var(--ink);
  }
</style>
</head>
<body>
  <main class="canvas">
    <section class="label">
      <div class="label__streaks"></div>
      <p class="label__kicker">Health Drink</p>
      <h1 class="label__title">Golden Reed Glow</h1>
      <p class="label__subtitle">Weight Loss Drink</p>
      <div class="label__athletes" role="img" aria-label="Photo of a fit man flexing his arms behind a fit woman in a side lunge, both in neon green sportswear, surrounded by golden light streaks"></div>
      <div class="label__facts">
        <ul class="facts__claims">
          <li class="facts__claim"><svg class="facts__tick" viewBox="0 0 12 12"><path d="M2 6.5 L5 9.5 L10 2.5" fill="none" stroke="#c8ff3c" stroke-width="2" stroke-linecap="round" stroke-linejoin="round"/></svg>Carb blocking</li>
          <li class="facts__claim"><svg class="facts__tick" viewBox="0 0 12 12"><path d="M2 6.5 L5 9.5 L10 2.5" fill="none" stroke="#c8ff3c" stroke-width="2" stroke-linecap="round" stroke-linejoin="round"/></svg>Calorie burning</li>
          <li class="facts__claim"><svg class="facts__tick" viewBox="0 0 12 12"><path d="M2 6.5 L5 9.5 L10 2.5" fill="none" stroke="#c8ff3c" stroke-width="2" stroke-linecap="round" stroke-linejoin="round"/></svg>100% natural</li>
          <li class="facts__claim"><svg class="facts__tick" viewBox="0 0 12 12"><path d="M2 6.5 L5 9.5 L10 2.5" fill="none" stroke="#c8ff3c" stroke-width="2" stroke-linecap="round" stroke-linejoin="round"/></svg>No sugar added</li>
        </ul>
        <p class="facts__heading">Flavours</p>
        <ul class="facts__flavours">
          <li class="facts__flavour">Refreshing Lemon</li>
          <li class="facts__flavour">Tropical Berry</li>
          <li class="facts__flavour">Smooth Strawberry</li>
        </ul>
      </div>
      <p class="label__volume">500ml</p>
    </section>
  </main>
</body>
</html>
```